The Brightwell Circle - Wordpress Web design and upload within 10 days

TO BE DESIGNED AND UPLOADED WITHIN 10 DAYS!

We have been burnt with a previous contractor and need urgent help please....

We have purchased a Wordpress template located at www.thebrightwellcircle.com.au that requires BOTH:

1. Wordpress website Design that compliments the new logo, sleek corporate sophisticated feel; AND
1a. The imbedding of your design into the existing wordpress template (gifs, jpegs uploaded - tested and working).

It is a small job - just needing a streamlined look and feel with easy/fast implementation.

Thank you kindly for your consideration and time.
Regards,
Moira
Updates

We are yet to receive the high res files, however please find attached logo thumbnails to get you started! 

Industry/Entity Type

Contractor

Font styles to use
Sans Serif

Colors

Designer to choose colors to be used in the design.

Requirements
Must have
• Please incorporate:
- NEW LOGO (file will be uploaded by COB today)
- Same colours and font as new logo
- Web page NON scrolling - 1200x800 max on laptop
- Designed to auto-fit any mobile device
- CLEAN WHITE SPACES that articulate a 'unique and sophisticated corporation'
- Upload immediately (no delays)
- A Contact page that has checkbox capabilities to quickly list interest in products/services with email box
- A 'genuine' Thank you page (reply) with a link for followup sent to me
- An EXPERIENCE page (grid/table page - 4 across) that lists logos of each company we have/will support
- PARTNERSHIPS page (grid/table page - 1 across) that lists logo on left with text on right
- NEWSLETTER page
- Area for Social media (Chatterly, Work Net, etc) and associated links
- Search box
- At top left of each page, an 'auto' 'Breadcrumb' for easy page referencing (i.e.: PRODUCTS .. TRAQ Profile .. Sales Mapping)

We like white, clean space giving viewers time to think but increasing their desire to want to view more and submit an easy checkbox of interest and request for contact.

We are open to any great ideas you have - we want a "corporate" difference that we are proud to promote as we are hoping to be in front of govt as well as clients. ;-D

MUST be easy to maintain of course.

Thank you.
Should not have
• Slow uploads - must be immediate please.

```html
<!DOCTYPE html>
<html lang="en">
<head>
<meta charset="utf-8">
<title>The Brightwell Circle</title>
<link rel="stylesheet" href="https://fonts.googleapis.com/css2?family=Source+Sans+3:wght@300;400;600;700&display=swap">
<style>
  :root {
    --red: #c8202a;
    --red-light: #d9343c;
    --red-dark: #a5141c;
    --ink: #3c3c3c;
    --ink-soft: #666666;
    --grey-mid: #8a8a8a;
    --grey-line: #dcdcdc;
    --panel: #eeeeee;
    --menu-top: #5a5a5a;
    --menu-bottom: #2c2c2c;
    --white: #ffffff;
  }
  * { box-sizing: border-box; margin: 0; padding: 0; }
  html, body { width: 1200px; height: 800px; overflow: hidden; background: var(--white); }
  body { position: relative; font-family: "Source Sans 3", Arial, sans-serif; color: var(--ink); }
  a { color: inherit; text-decoration: none; }

  .site-header { position: absolute; left: 0; top: 0; width: 1200px; height: 85px; }
  .brand { position: absolute; left: 122px; top: 24px; display: flex; align-items: center; gap: 12px;
           font-size: 28px; font-weight: 600; color: var(--ink); letter-spacing: -0.3px; }
  .brand-mark { width: 26px; height: 26px; background: var(--red); }
  .social { position: absolute; left: 966px; top: 27px; display: flex; gap: 8px; }
  .social-link { width: 32px; height: 32px; border-radius: 50%; background: var(--grey-mid); display: block; }

  .main-nav { position: absolute; left: 0; top: 85px; width: 1200px; height: 46px;
              background: linear-gradient(var(--red-light), var(--red-dark)); }
  .nav-list { position: absolute; left: 122px; top: 0; display: flex; list-style: none; height: 46px; }
  .nav-item { height: 46px; border-right: 1px solid #8e1017; box-shadow: 1px 0 0 rgba(255,255,255,0.15);
              color: var(--white); font-weight: 600; font-size: 15.5px; text-transform: uppercase;
              display: flex; align-items: center; justify-content: center; }
  .nav-item.is-active { background: #3a3a3a; }
  .search { position: absolute; left: 891px; top: 8px; width: 189px; height: 30px; background: var(--white);
            font-size: 13px; color: #999; padding: 6px 11px; }
  .search svg { position: absolute; right: 10px; top: 7px; }

  .dropdown { position: absolute; left: 121px; top: 129px; width: 188px; height: 214px; z-index: 5;
              background: linear-gradient(var(--menu-top), var(--menu-bottom)); list-style: none;
              box-shadow: 0 2px 4px rgba(0,0,0,0.3); padding-top: 14px; }
  .dropdown li { height: 40px; padding-left: 22px; color: var(--white); font-size: 15px; }
  .dropdown li::before { content: "»"; margin-right: 6px; }

  .hero { position: absolute; left: 120px; top: 175px; width: 960px; height: 338px;
          background: var(--panel); border: 1px solid var(--grey-line); }
  .hero-inner { position: absolute; left: 7px; top: 7px; width: 944px; height: 322px; background: var(--white); overflow: hidden; }
  .hero-photo { position: absolute; right: 0; top: 0; width: 480px; height: 322px;
                background: linear-gradient(90deg, #ffffff 0%, #e8e4df 25%, #c9c2b8 60%, #a9a49d 100%); }
  .hero-title { position: absolute; left: 43px; top: 40px; line-height: 1; font-weight: 300; }
  .hero-title .welcome { color: var(--red); font-size: 40px; }
  .hero-title .to { color: var(--red); font-size: 28px; }
  .hero-title .name { display: block; color: var(--ink); font-size: 30px; margin-top: 8px; }
  .hero-text { position: absolute; left: 43px; top: 133px; width: 360px; font-size: 14px; line-height: 22px; color: var(--ink-soft); }
  .btn-more { position: absolute; left: 44px; top: 212px; width: 98px; height: 33px;
              background: linear-gradient(#777, #4a4a4a); color: var(--white); font-size: 13.5px;
              border-radius: 2px; display: flex; align-items: center; justify-content: center; }
  .pager { position: absolute; left: 42px; top: 279px; display: flex; gap: 10px; }
  .pager span { width: 14px; height: 14px; border-radius: 50%; background: #cfcfcf; }
  .pager span.is-current { background: #9a9a9a; }

  .features { position: absolute; top: 540px; list-style: none; }
  .features.col-a { left: 124px; }
  .features.col-b { left: 518px; }
  .feature { height: 49.5px; display: flex; align-items: center; font-size: 19.5px; color: var(--ink); }
  .feature svg { width: 32px; margin-right: 13px; flex: none; }
  .feature.is-highlight { color: var(--red); }

  .promo { position: absolute; left: 813px; top: 543px; width: 266px; height: 171px;
           border: 1px solid var(--grey-line); border-radius: 2px; overflow: hidden;
           background: linear-gradient(#ffffff, #eeeeee); }
  .promo-photo { position: absolute; left: 0; top: 20px; width: 150px; height: 151px;
                 background: linear-gradient(#f2f2f2, #c7c7c7 50%, #a42a2c 80%, #8c2225); }
  .promo-title { position: absolute; right: 13px; top: 12px; text-align: right; font-size: 23px;
                 line-height: 26px; color: #9a9a9a; }
  .btn-join { position: absolute; left: 151px; top: 76px; width: 98px; height: 34px; border-radius: 3px;
              background: linear-gradient(var(--red-light), var(--red-dark)); color: var(--white);
              font-size: 13px; font-weight: 600; display: flex; align-items: center; justify-content: center;
              box-shadow: 0 2px 3px rgba(0,0,0,0.25); }

  .site-footer { position: absolute; left: 0; top: 742px; width: 1200px; height: 58px;
                 background: var(--panel); border-top: 1px solid var(--grey-line); }
  .footer-nav { position: absolute; left: 121px; top: 19px; display: flex; list-style: none; font-size: 13px; color: var(--ink-soft); }
  .footer-nav li + li::before { content: "|"; color: #bbb; margin: 0 9px; }
  .copyright { position: absolute; right: 121px; top: 19px; font-size: 13px; color: var(--ink-soft); word-spacing: 2px; }
</style>
</head>
<body>
  <header class="site-header">
    <a class="brand" href="#"><span class="brand-mark"></span>The Brightwell Circle</a>
    <nav class="social" aria-label="Social media">
      <a class="social-link" href="#" aria-label="Chatterly"></a>
      <a class="social-link" href="#" aria-label="Chirpline"></a>
      <a class="social-link" href="#" aria-label="Work Net"></a>
    </nav>
  </header>

  <nav class="main-nav">
    <ul class="nav-list">
      <li class="nav-item is-active" style="width:86px">Home</li>
      <li class="nav-item" style="width:103px">Services</li>
      <li class="nav-item" style="width:113px">Products</li>
      <li class="nav-item" style="width:109px">Research</li>
      <li class="nav-item" style="width:141px">Associations</li>
      <li class="nav-item" style="width:91px">Join Us</li>
      <li class="nav-item" style="width:102px">Contact</li>
    </ul>
    <div class="search">Search
      <svg width="16" height="16" viewBox="0 0 16 16"><circle cx="6" cy="6" r="4.5" fill="none" stroke="#222" stroke-width="2"/><line x1="9.5" y1="9.5" x2="14.5" y2="14.5" stroke="#222" stroke-width="3" stroke-linecap="round"/></svg>
    </div>
  </nav>

  <ul class="dropdown">
    <li>Our Story</li>
    <li>Our Experience</li>
    <li>Our Specialists</li>
    <li>Client Testimonials</li>
    <li>Your Q&amp;A</li>
  </ul>

  <section class="hero">
    <div class="hero-inner">
      <div class="hero-photo" role="img" aria-label="Smiling businessman holding glasses in a bright office"></div>
      <h1 class="hero-title"><span class="welcome">Welcome</span> <span class="to">to</span><span class="name">The Brightwell Circle</span></h1>
      <p class="hero-text">Nunc egestas dolor sit lorem, nec luctus nibh lacinia eget. Nullam sagittis, purus quis venenatis pretium, nibh magna faucibus quam, et elementum risus libero ac urna.</p>
      <a class="btn-more" href="#">KNOW MORE</a>
      <div class="pager"><span class="is-current"></span><span></span><span></span><span></span></div>
    </div>
  </section>

  <ul class="features col-a">
    <li class="feature is-highlight">
      <svg height="26" viewBox="0 0 32 26"><text x="10" y="22" font-family="Arial, sans-serif" font-size="24" font-weight="700" fill="#c8202a">$</text></svg>Grands &amp; Funding</li>
    <li class="feature">
      <svg height="26" viewBox="0 0 32 26" fill="none" stroke="#3c3c3c" stroke-width="1.6"><path d="M2 5h16v10H8l-4 4v-4H2z"/><path d="M12 9h18v10h-2v4l-4-4H12z" fill="#fff"/></svg>Post-GFC Business &amp; HR Consulting</li>
    <li class="feature">
      <svg height="26" viewBox="0 0 32 26" fill="#3c3c3c"><path d="M1 6c5-2 10-2 14 1v15c-4-3-9-3-14-1z"/><path d="M31 6c-5-2-10-2-14 1v15c4-3 9-3 14-1z"/></svg>Nationally Accredited Education</li>
    <li class="feature">
      <svg height="30" viewBox="0 0 32 30" fill="#3c3c3c"><circle cx="16" cy="9" r="7"/><path d="M11 14l-2 14 4-3 3 4 1-14zM21 14l2 14-4-3-3 4-1-14z"/></svg>Certificate IV</li>
  </ul>

  <ul class="features col-b">
    <li class="feature">
      <svg height="26" viewBox="0 0 32 26" fill="#3c3c3c"><path d="M7 2a5 5 0 0 0-2 7l-1 1 1 1 1-1a5 5 0 0 0 6 -1l12 12a2 2 0 0 0 3-3L15 6a5 5 0 0 0-4-5l-2 3 1 2-2 1-2-1z"/></svg>Trainning &amp; Development</li>
    <li class="feature">
      <svg height="26" viewBox="0 0 32 26" fill="#3c3c3c"><circle cx="10" cy="7" r="5"/><path d="M2 24c0-7 4-10 8-10s8 3 8 10z"/><circle cx="22" cy="9" r="4.5"/><path d="M16 24c0-6 3-9 6-9s7 3 7 9z"/></svg>Coaching</li>
    <li class="feature">
      <svg height="26" viewBox="0 0 32 26" fill="#3c3c3c"><rect x="3" y="14" width="4" height="9"/><rect x="9" y="9" width="4" height="14"/><rect x="15" y="16" width="4" height="7"/><rect x="21" y="11" width="4" height="12"/><rect x="27" y="4" width="3" height="19"/></svg>Management Audits</li>
  </ul>

  <aside class="promo">
    <div class="promo-photo" role="img" aria-label="Excited man at a laptop raising his fist"></div>
    <p class="promo-title">Fusce pretium<br>ante vitae</p>
    <a class="btn-join" href="#">JOIN WITH US</a>
  </aside>

  <footer class="site-footer">
    <ul class="footer-nav">
      <li>Home</li><li>Services</li><li>Products</li><li>Research</li><li>Associations</li><li>Join Us</li><li>Contact</li>
    </ul>
    <p class="copyright">Copyright © 2013 The Brightwell Circle. All rights reserved.</p>
  </footer>
</body>
</html>
```